Baby Care Print Log for Nannies and Parents- Creating a brand/style I can use across different forms

I am creating a notebook for babysitters to use to communicate with parents about the children they care for. I will be creating many different forms (emergency contacts, daily logs, shopping lists, etc.)
I need a look and feel from which to style these forms from. I am starting by designing the daily baby care log. I need a designer to take my Word doc with just text on it, and create a visual approach to make this visually appealing.
I do not want this to be extremely "babyish" with cartoon styling. I want it to be more of a professional looking style. I would like to be able to color each different document a different color palette, yet keep the similar look and feel. My logo is attached for inspiration. I use real photography across my website velmorapath.com.
Updates
I will be re-designing my Wordpress website based on what design I like best and also will need other forms completed once I pick a design. I am hoping to work with someone who I can hire for further development needs as well. Added Saturday, February 11, 2017
Target Market(s)
Professional Parents
Industry/Entity Type
Education
Requirements
Must have
- color, pop, visual appeal
- Please use the color in my logo and any complementary colors that you think work well with it. I definitely like colored patterns, ombre, colored backgrounds, etc. I'd prefer for it not to be completely white with only pops of color here and there.
Nice to have
- My logo somewhere subtly on the form
- Photography elements
Should not have
- cartoon images of babies, etc. I use real photography across my website with the exception of my logo umbrella.

```html
<!DOCTYPE html>
<html lang="en">
<head>
<meta charset="utf-8">
<title>Velmora Path – Daily Baby Care Log</title>
<link href="https://fonts.googleapis.com/css2?family=Roboto+Condensed:wght@400;700&display=swap" rel="stylesheet">
<style>
  :root {
    --teal: #1fa3c0;
    --sky: #3ec3e0;
    --deep: #25aec2;
    --row-dark: #c2e7ef;
    --row-light: #e7f6fb;
    --ink: #555;
    --title: #222;
    --backdrop: #b0b0b0;
  }
  * { margin: 0; padding: 0; box-sizing: border-box; }
  html, body { width: 1200px; height: 1200px; overflow: hidden; background: var(--backdrop); }
  body { position: relative; font-family: "Roboto Condensed", sans-serif; }
  .sheet {
    position: absolute; left: 136px; top: 0;
    width: 863px; height: 1117px; background: #fff;
    transform: scale(1.0743); transform-origin: top left; overflow: hidden;
  }
  .abs { position: absolute; }
  .bands { position: absolute; left: 0; top: 0; }
  .photo { position: absolute; border-radius: 40% 40% 20% 20%; }
  .photo-top { left: 160px; top: 28px; width: 168px; height: 155px;
    background: radial-gradient(circle at 45% 35%, #f3cdb4 0 30%, #f7ece6 55%, #fff 80%); }
  .photo-bottom { left: 620px; top: 900px; width: 243px; height: 215px;
    background: radial-gradient(circle at 40% 35%, #f1c3a6 0 35%, #f5dccd 60%, rgba(255,255,255,0) 80%); }
  .brand { left: 345px; top: 100px; display: flex; align-items: center; gap: 14px; }
  .brand-dot { width: 34px; height: 34px; border-radius: 50%; background: var(--sky); }
  .brand-name { font-size: 46px; font-weight: 700; color: var(--title); }
  .label { color: var(--teal); font-weight: 700; font-size: 16px; }
  .heading { color: var(--teal); font-weight: 700; font-size: 19px; }
  .dotline { position: absolute; border-bottom: 1.5px dotted var(--teal); }
  table.log { position: absolute; border-collapse: collapse; border: 1px solid var(--sky); table-layout: fixed; }
  table.log th.head { background: var(--sky); color: #fff; font-size: 19px; height: 32px; font-weight: 700; }
  table.log th.col { background: var(--row-light); color: var(--teal); font-weight: 400; font-size: 15px; height: 30px; }
  table.log td { height: 29px; border-right: 2px solid #fff; }
  table.log th.col { border-right: 2px solid #fff; border-bottom: 1px solid #d6eef4; }
  table.log tr:nth-child(odd) td { background: var(--row-dark); }
  table.log tr:nth-child(even) td { background: var(--row-light); }
  table.log td:last-child, table.log th.col:last-child { border-right: none; }
  .row-label { font-size: 15px; color: var(--ink); }
  .box { position: absolute; width: 25px; height: 24px; border: 1.5px solid var(--teal); border-radius: 3px; }
  .dash { position: absolute; width: 38px; border-bottom: 1.5px dashed var(--teal); }
  .mood-icon { position: absolute; width: 38px; height: 38px; border-radius: 50%; background: var(--sky); border: 2px solid #fff; box-shadow: 0 0 0 1.5px var(--sky); }
  .mood-label { position: absolute; font-size: 15px; color: var(--ink); transform: translateX(-50%); white-space: nowrap; }
  .supply { position: absolute; font-size: 15px; color: var(--ink); }
</style>
</head>
<body>
<main class="sheet">
  <svg class="bands" width="863" height="1117" viewBox="0 0 863 1117">
    <polygon points="412,0 863,0 863,103" fill="var(--sky)"/>
    <polygon points="412,0 863,70 863,103" fill="var(--deep)"/>
    <polygon points="0,1027 830,1110 0,1117" fill="var(--deep)"/>
    <polygon points="0,1050 863,1117 0,1117" fill="var(--sky)"/>
  </svg>

  <div class="photo photo-top" role="img" aria-label="Photo of a smiling baby lying on its tummy"></div>

  <div class="abs brand"><span class="brand-dot"></span><span class="brand-name">Velmora Path</span></div>

  <span class="abs label" style="left:91px;top:202px">Name:</span>
  <div class="dotline" style="left:147px;top:208px;width:354px"></div>
  <span class="abs label" style="left:529px;top:202px">Date:</span>
  <div class="dotline" style="left:574px;top:208px;width:198px"></div>

  <table class="log" style="left:91px;top:244px;width:290px">
    <colgroup><col style="width:86px"><col></colgroup>
    <tr><th class="head" colspan="2">Nap Time</th></tr>
    <tr><th class="col">Time</th><th class="col" style="text-align:left;padding-left:20px">How Long</th></tr>
    <tr><td></td><td></td></tr><tr><td></td><td></td></tr><tr><td></td><td></td></tr>
    <tr><td></td><td></td></tr><tr><td></td><td></td></tr><tr><td></td><td></td></tr>
  </table>

  <table class="log" style="left:405px;top:244px;width:367px">
    <colgroup><col style="width:61px"><col style="width:81px"><col style="width:80px"><col style="width:76px"><col></colgroup>
    <tr><th class="head" colspan="5">Feeding</th></tr>
    <tr><th class="col">Time</th><th class="col">Milk(Type)</th><th class="col">Water</th><th class="col">Food</th><th class="col">Amount</th></tr>
    <tr><td></td><td></td><td></td><td></td><td></td></tr><tr><td></td><td></td><td></td><td></td><td></td></tr>
    <tr><td></td><td></td><td></td><td></td><td></td></tr><tr><td></td><td></td><td></td><td></td><td></td></tr>
    <tr><td></td><td></td><td></td><td></td><td></td></tr><tr><td></td><td></td><td></td><td></td><td></td></tr>
  </table>

  <span class="abs heading" style="left:91px;top:503px">Diapers</span>
  <span class="abs row-label" style="left:91px;top:544px">Time</span>
  <div class="dash" style="left:133px;top:556px"></div><div class="dash" style="left:180px;top:556px"></div>
  <div class="dash" style="left:226px;top:556px"></div><div class="dash" style="left:273px;top:556px"></div>
  <div class="dash" style="left:319px;top:556px"></div><div class="dash" style="left:366px;top:556px"></div>
  <div class="dash" style="left:412px;top:556px"></div><div class="dash" style="left:459px;top:556px"></div>
  <span class="abs row-label" style="left:91px;top:587px">Wet</span>
  <div class="box" style="left:140px;top:584px"></div><div class="box" style="left:187px;top:584px"></div>
  <div class="box" style="left:233px;top:584px"></div><div class="box" style="left:280px;top:584px"></div>
  <div class="box" style="left:326px;top:584px"></div><div class="box" style="left:373px;top:584px"></div>
  <div class="box" style="left:419px;top:584px"></div><div class="box" style="left:466px;top:584px"></div>
  <span class="abs row-label" style="left:91px;top:631px">BM</span>
  <div class="box" style="left:140px;top:628px"></div><div class="box" style="left:187px;top:628px"></div>
  <div class="box" style="left:233px;top:628px"></div><div class="box" style="left:280px;top:628px"></div>
  <div class="box" style="left:326px;top:628px"></div><div class="box" style="left:373px;top:628px"></div>
  <div class="box" style="left:419px;top:628px"></div><div class="box" style="left:466px;top:628px"></div>

  <span class="abs heading" style="left:537px;top:503px">Mood</span>
  <div class="mood-icon" style="left:538px;top:535px"></div><span class="mood-label" style="left:557px;top:576px">Happy</span>
  <div class="mood-icon" style="left:592px;top:535px"></div><span class="mood-label" style="left:612px;top:576px">Sad</span>
  <div class="mood-icon" style="left:660px;top:535px"></div><span class="mood-label" style="left:682px;top:576px">Unsettled</span>
  <div class="mood-icon" style="left:538px;top:603px"></div><span class="mood-label" style="left:566px;top:641px">Energetic</span>
  <div class="mood-icon" style="left:612px;top:602px"></div><span class="mood-label" style="left:631px;top:641px">Tired</span>
  <div class="mood-icon" style="left:673px;top:606px"></div><span class="mood-label" style="left:691px;top:641px">Chatty</span>
  <div class="mood-icon" style="left:729px;top:606px"></div><span class="mood-label" style="left:751px;top:641px">Quiet</span>

  <span class="abs heading" style="left:91px;top:679px">Today’s Activities</span>

  <span class="abs heading" style="left:93px;top:785px">Supplies Needed Soon</span>
  <div class="box" style="left:93px;top:821px"></div><span class="supply" style="left:132px;top:823px">Diapers</span>
  <div class="box" style="left:93px;top:850px"></div><span class="supply" style="left:132px;top:852px">Diaper Cream</span>
  <div class="box" style="left:93px;top:880px"></div><span class="supply" style="left:132px;top:882px">Other:</span>
  <div class="box" style="left:318px;top:821px"></div><span class="supply" style="left:356px;top:823px">Milk/Formula</span>
  <div class="box" style="left:318px;top:850px"></div><span class="supply" style="left:356px;top:852px">Cereal</span>
  <div class="box" style="left:522px;top:821px"></div><span class="supply" style="left:563px;top:823px">Wet Wipes</span>
  <div class="box" style="left:522px;top:850px"></div><span class="supply" style="left:563px;top:852px">Baby Food</span>

  <span class="abs label" style="left:94px;top:926px">Special Notes</span>
  <div class="dotline" style="left:198px;top:938px;width:490px"></div>
  <div class="dotline" style="left:94px;top:966px;width:594px"></div>
  <div class="dotline" style="left:94px;top:995px;width:594px"></div>
  <div class="dotline" style="left:94px;top:1024px;width:570px"></div>

  <div class="photo photo-bottom" role="img" aria-label="Photo of a laughing baby lying on its tummy"></div>
</main>
</body>
</html>
```